Seeking Artist For The Design of a Series of Soft & Hard Cover Spiritual Books

A small internationally known contemplative spiritual organization seeks the services of a expert graphic designer, preferably with experience in book jacket design, to assist the organization in repackaging a series of six books that already sell in the market place. The new book jacket design, will carry a more contemporary theme reflective of some of the extremely popular bestsellers on spirituality & self-improvement such as "The Lantern and Drift".

For this project, we would like the artist to create a book jacket using Sanskrit graphics (see attached) in the background. We will ask that they look at the book jacket, “The Lantern” to see an example of a jacket that we like. We are hoping for a similar look through the use of the Sanskrit lettering in the background. Please note on the book jacket of The Lantern, the words float off the page, the seal also seem elevated and there seems to be an aura illuminating the cover. We really like this kind of three-dimensional affect.

We would also like for you to consider a way to identify this as the first book in a series on the front of the cover and on the spine of the book so that when it sits on the shelf as a series, the reader can see (perhaps using a color code) them as a series.

Terms to help you understand the cultural context of the books include:
Consciousness, Meditation, Spiritual, Tantric, Eastern, Shiva, Yoga, Enlightenment, Wisdom, Self-Realization, Self-Improvement, Self-Actualization…

Please note that we like serif font, would like to stay away from San Serif for this project. Also please note there are diacritical marks in the title.

Title:
Murmur of the Distant Shore
Durvasendra's Vyomakāntikā
revealed by Swami Ravindrashan
The Ravindrashan Academy Book Series

Reason: Hi, thank you for all the wonderful designs you have already submitted, we will be extending the deadline another week so we get more time to decide and also to give some more designers a chance to submit. Thank you Marisol

Reason: Thank you for all the wonderful designs you have submitted so far. Sorry for the lack of response, we just finished our in-house retreat and need a few more days to recover. Thank you for your understanding. Warm Regards Marisol

```html
<!DOCTYPE html>
<html lang="en">
<head>
<meta charset="utf-8">
<title>Murmur of the Distant Shore — Book Jacket</title>
<link rel="stylesheet" href="https://fonts.googleapis.com/css2?family=Kurale&display=swap">
<style>
  :root {
    --backdrop: #ececec;
    --cover: #050505;
    --spine: #0b0b0b;
    --glow-orange: #ff9a1f;
    --glow-deep: #e86a00;
    --title-fill: #fff4d6;
    --ink-white: #f4f4f4;
    --ink-grey: #9a9a9a;
    --ink-dim: #6a6a6a;
    --placeholder: #151515;
  }
  * { box-sizing: border-box; margin: 0; padding: 0; }
  html, body { width: 1200px; height: 800px; overflow: hidden; }
  body {
    background: var(--backdrop);
    font-family: "Kurale", serif;
    text-transform: lowercase;
    position: relative;
  }
  .jacket {
    position: absolute;
    left: 162px; top: 80px;
    width: 876px; height: 640px;
    display: flex;
    box-shadow: 0 18px 40px rgba(0,0,0,0.25);
  }
  .back-cover, .front-cover {
    width: 420px; height: 100%;
    background: var(--cover);
    position: relative;
    text-align: center;
  }
  .spine {
    width: 36px; height: 100%;
    background: var(--spine);
    border-left: 1px solid #1c1c1c;
    border-right: 1px solid #1c1c1c;
    display: flex; align-items: center; justify-content: center;
  }
  .spine-title {
    writing-mode: vertical-rl;
    color: var(--glow-orange);
    font-size: 18px;
    letter-spacing: 0.5px;
    white-space: nowrap;
    text-shadow: 0 0 4px var(--glow-deep);
  }
  .glow-title {
    font-weight: 400;
    color: var(--title-fill);
    -webkit-text-stroke: 1.5px var(--glow-orange);
    text-shadow:
      0 0 4px var(--glow-orange),
      0 0 10px var(--glow-orange),
      0 0 18px var(--glow-deep);
    line-height: 0.98;
  }
  /* front */
  .front-cover .credit {
    padding-top: 12px;
    color: var(--ink-white);
    font-size: 20px;
    letter-spacing: 0.5px;
  }
  .front-cover .glow-title {
    margin-top: 14px;
    font-size: 72px;
  }
  .light-in-hands {
    width: 220px; height: 150px;
    margin: 20px auto 0;
    background: radial-gradient(ellipse at 52% 42%, #fff7d8 0%, #ffc65a 12%, #b0641c 32%, #4a2a10 55%, var(--cover) 78%);
  }
  .front-cover .subtitle {
    position: absolute; left: 0; right: 0; bottom: 58px;
    color: var(--ink-white);
    font-size: 21px;
  }
  .front-cover .series {
    position: absolute; left: 0; right: 0; bottom: 24px;
    color: var(--ink-white);
    font-size: 17px;
    letter-spacing: 0.3px;
  }
  /* back */
  .back-cover .credit {
    padding-top: 16px;
    color: var(--ink-dim);
    font-size: 11px;
  }
  .back-cover .glow-title {
    margin-top: 4px;
    font-size: 38px;
  }
  .blurb {
    margin: 22px 32px 0;
    color: var(--ink-grey);
    font-size: 14px;
    line-height: 1.62;
    text-align: justify;
  }
  .back-footer {
    position: absolute; left: 38px; right: 38px; bottom: 14px;
    display: flex; justify-content: space-between;
  }
  .placeholder-box {
    width: 88px; height: 58px;
    background: var(--placeholder);
    color: var(--ink-dim);
    font-size: 10px;
    display: flex; align-items: center; justify-content: center;
  }
</style>
</head>
<body>
  <div class="jacket">
    <section class="back-cover">
      <p class="credit">revealed by Swami Ravindrashan</p>
      <h2 class="glow-title">Murmur of<br>the Distant Shore</h2>
      <p class="blurb">In this luminous commentary the master unfolds each verse of an ancient text on the nature of consciousness, guiding the reader from the outer world of forms toward the silent awareness that shines within every moment. Drawing on a lifetime of practice, he explains how bondage and freedom are two movements of one light, and how the seeker may rest in that light through meditation, devotion and understanding. The verses speak of the self as a vast sky in which all appearances rise and dissolve, and of the teacher's grace as the breeze that clears the clouds. Clear, warm and direct, these talks offer both the newcomer and the long practitioner a path toward lasting peace and wisdom. Here the old teaching becomes a living voice for our own time, inviting each reader to discover the shore that was never distant.</p>
      <div class="back-footer">
        <div class="placeholder-box">logo</div>
        <div class="placeholder-box">isbn</div>
      </div>
    </section>

    <div class="spine">
      <span class="spine-title">Murmur of the Distant Shore</span>
    </div>

    <section class="front-cover">
      <p class="credit">revealed by Swami Ravindrashan</p>
      <h1 class="glow-title">Murmur<br>of the<br>Distant<br>Shore</h1>
      <div class="light-in-hands" role="img" aria-label="Photograph of cupped hands holding a bright burst of light"></div>
      <p class="subtitle">Durvasendra's Vyomakāntikā</p>
      <p class="series">The Ravindrashan Academy Book Series</p>
    </section>
  </div>
</body>
</html>
```